Travel Agency Website - Simple General

Need a 7 page simple design that is pretty repetitive. Need to be able to load quickly that is SEO optimized. Trying to give ideas on what they can do, be personal as we are local, but at the same time come across as professional and get information easily with little burden.

- Landing Page
- Brambleton Vacations Page
- Family Trips
- Road Trips from Texas
- Other Destinations
- About Us Page
- Contact Us Page

Target Market(s)

Families

Coding

Coded - Design and coding required

Number of Pages Required

5+ page

Colors

Designer to choose colors to be used in the design.

Requirements
Must have
• Like it to flow easily with our logo. Use that for colors, etc.

```html
<!DOCTYPE html>
<html lang="en">
<head>
<meta charset="utf-8">
<title>Meander &amp; Maple Travel Co. — Your Next Adventure Planned with Heart</title>
<meta name="viewport" content="width=1200">
<link href="https://fonts.googleapis.com/css2?family=Gloock&family=Montserrat:wght@400;500;600;700&display=swap" rel="stylesheet">
<style>
:root{
  --teal:#1d5566;
  --teal-deep:#16495a;
  --footer:#21606f;
  --gold:#c0923f;
  --gold-soft:#c6a06a;
  --cream:#fbf8f2;
  --sage:#e1e9e3;
  --tan:#c9ab7d;
  --white:#ffffff;
  --ink:#23404a;
}
*{box-sizing:border-box;margin:0;padding:0}
html,body{width:1200px;height:3333px;overflow:hidden}
body{position:relative;background:var(--cream);font-family:"Montserrat",Arial,sans-serif;color:var(--teal)}
.abs{position:absolute}
.serif{font-family:"Gloock",Georgia,serif;font-weight:400}
.photo{position:absolute}

/* header */
.hero-bg{left:0;top:0;width:1200px;height:760px;background:linear-gradient(180deg,#d9d3c8 0%,#e8dfd0 25%,#d8c3a2 45%,#c9b08c 62%,#efe7da 86%,var(--cream) 100%)}
.brand{left:119px;top:36px;width:124px;height:50px;display:flex;align-items:center;gap:6px;font-weight:700;font-size:15px;line-height:1.1;color:var(--teal)}
.brand-dot{width:10px;height:10px;border-radius:50%;background:var(--gold);flex:none}
.nav{left:325px;top:49px;display:flex;gap:19px;font-size:10.5px;font-weight:600;letter-spacing:.2px;color:var(--teal)}
.btn-contact{left:967px;top:43px;width:114px;height:25px;background:var(--gold);color:var(--white);font-size:10.5px;font-weight:600;display:flex;align-items:center;justify-content:center}

.hero-kicker{left:330px;top:178px;font-size:37px;color:var(--gold)}
.hero-title{left:120px;top:196px;font-size:86px;line-height:1;color:var(--teal)}
.hero-sub{left:120px;top:270px;font-size:48px;color:var(--teal)}
.hero-lede{left:122px;top:326px;font-size:14px;color:var(--ink)}
.btn-start{left:120px;top:368px;width:236px;height:33px;background:var(--white);display:flex;align-items:center;justify-content:center;gap:10px;font-size:11px;font-weight:600;color:var(--teal)}

.play{left:546px;top:611px;width:72px;height:72px}

/* tagline */
.tagline{left:100px;top:900px;width:1000px;text-align:center;font-size:39px;line-height:41px;color:var(--teal)}

/* category cards */
.card{top:1069px;width:230px;height:273px}
.card-shade{position:absolute;left:0;right:0;bottom:0;height:150px;background:linear-gradient(180deg,rgba(14,50,60,0) 0%,rgba(14,50,60,.85) 55%,#0f3540 100%)}
.card-title{position:absolute;left:0;right:0;top:176px;text-align:center;color:var(--white);font-weight:600;font-size:18px;line-height:22px}
.card-sub{position:absolute;left:0;right:0;top:229px;text-align:center;color:var(--white);font-size:11px}
.card-plus{position:absolute;left:102px;top:260px;width:26px;height:26px;border-radius:50%;background:var(--gold);color:var(--white);font-size:16px;line-height:26px;text-align:center;font-weight:600}

/* why choose */
.why{left:0;top:1396px;width:1200px;height:394px;background:var(--sage)}
.eyebrow{font-size:13px;font-weight:600;letter-spacing:.5px;color:var(--gold)}
.why-title{left:114px;top:1470px;width:980px;font-size:39px;line-height:41px;color:var(--teal)}
.feature{top:1603px;width:314px;height:136px;background:var(--cream)}
.feature svg{position:absolute;left:14px;top:36px}
.feature-title{position:absolute;left:91px;top:26px;font-size:15px;font-weight:700;line-height:20px;letter-spacing:.3px}
.feature-text{position:absolute;left:91px;top:76px;width:200px;font-size:11px;line-height:15px;color:var(--ink)}
.feature-num{position:absolute;right:16px;top:8px;font-size:46px;color:var(--gold-soft)}

/* community */
.community{left:0;top:1790px;width:1200px;height:460px;background:linear-gradient(90deg,#9a8a5e 0%,#7d7a58 25%,#3e6468 50%,#1f5a68 70%,var(--teal) 100%)}
.community-title{left:610px;top:1910px;font-size:40px;line-height:42px;color:var(--white)}
.community-text{left:610px;top:2020px;width:440px;font-size:18px;line-height:21px;color:#e6eef0}
.btn-light{background:var(--white);color:var(--teal);font-size:11.5px;font-weight:600;display:flex;align-items:center;justify-content:center}

/* blogs */
.blogs-head{left:125px;top:2303px;font-size:18px;letter-spacing:.5px}
.view-all{left:994px;top:2305px;font-size:10.5px;font-weight:600;display:flex;align-items:center;gap:6px}
.blog{top:2360px;width:310px}
.blog .photo{position:relative;width:310px;height:136px}
.blog-title{margin-top:16px;font-size:14.5px;font-weight:600;line-height:17px;color:var(--teal)}
.blog-more{margin-top:14px;font-size:9.5px;font-weight:600;color:var(--gold);text-decoration:underline}

/* cta */
.cta-photo{left:16px;top:2750px;width:1184px;height:334px;background:linear-gradient(90deg,#2e3a3a 0%,#4b5350 30%,#6b5e4a 55%,#a0886a 75%,#3c3833 100%)}
.cta-box{left:383px;top:2666px;width:424px;height:277px;background:var(--tan)}
.cta-badge{left:535px;top:2650px;width:130px;height:60px;background:var(--cream);border-radius:30px;display:flex;align-items:center;justify-content:center;gap:6px;font-weight:700;font-size:13px;color:var(--teal)}
.cta-title{left:403px;top:2738px;width:384px;text-align:center;font-size:28px;line-height:30px;color:var(--white)}
.cta-text{left:403px;top:2842px;width:384px;text-align:center;font-size:11.5px;line-height:15px;color:var(--white)}
.btn-teal{left:487px;top:2887px;width:198px;height:36px;background:var(--teal);color:var(--white);font-size:14px;font-weight:700;display:flex;align-items:center;justify-content:center}

/* footer */
.footer{left:0;top:3084px;width:1200px;height:249px;background:var(--footer)}
.footer-brand{left:180px;top:3140px;width:150px;height:72px;background:var(--cream);border-radius:36px;display:flex;align-items:center;justify-content:center;gap:6px;font-weight:700;font-size:14px;color:var(--teal)}
.social{top:3244px;width:26px;height:26px;border-radius:50%;background:var(--gold-soft)}
.foot-col{top:3110px;color:var(--white)}
.foot-col h4{font-size:11px;font-weight:700;letter-spacing:.4px;margin-bottom:24px}
.foot-col li{list-style:none;font-size:11px;line-height:19.4px}
.contact-line{display:flex;align-items:center;gap:14px;margin-bottom:10px}
.contact-icon{width:24px;height:24px;border-radius:50%;background:var(--gold-soft);display:flex;align-items:center;justify-content:center}
.phone{font-size:18px}
.email{font-size:12px;text-decoration:underline}
.copyright{left:0;top:3294px;width:1200px;text-align:center;font-size:11px;color:#dfe9ec}
</style>
</head>
<body>

<!-- hero -->
<div class="abs hero-bg" role="img" aria-label="Sunlit lakeside boardwalk with a family strolling past waterfront villas at golden hour"></div>

<header>
  <a class="abs brand" href="#"><span class="brand-dot"></span><span>Meander &amp; Maple Travel Co.</span></a>
  <nav class="abs nav">
    <span>BRAMBLETON VACATIONS</span><span>FAMILY TRIPS</span><span>TEXAS ROAD TRIPS</span><span>OTHER DESTINATIONS</span><span>ABOUT US</span>
  </nav>
  <a class="abs btn-contact" href="#">CONTACT US</a>
</header>

<section class="hero">
  <div class="abs serif hero-kicker">Your Next</div>
  <h1 class="abs serif hero-title">Adventure</h1>
  <div class="abs serif hero-sub">Planned with Heart</div>
  <p class="abs hero-lede">Local travel experts helping you explore stress-free</p>
  <a class="abs btn-start" href="#">START PLANNING YOUR TRIP
    <svg width="18" height="10" viewBox="0 0 18 10"><path d="M0 5h16M12 1l4 4-4 4" fill="none" stroke="#1d5566" stroke-width="1.5"/></svg>
  </a>

  <div class="photo" style="left:122px;top:498px;width:227px;height:255px;background:linear-gradient(160deg,#b59a66,#7d6b45 60%,#4d4634)" role="img" aria-label="Mother hugging her young son by the water at sunset"></div>
  <div class="photo" style="left:367px;top:456px;width:426px;height:387px;background:linear-gradient(180deg,#2f4b55 0%,#8a8a86 30%,#5b4b3d 60%,#2f302b 100%)" role="img" aria-label="Couple toasting with drinks on a boat deck, video preview"></div>
  <svg class="abs play" viewBox="0 0 72 72"><circle cx="36" cy="36" r="33" fill="rgba(255,255,255,.18)" stroke="#fff" stroke-width="3"/><path d="M28 22l22 14-22 14z" fill="#fff"/></svg>
  <div class="photo" style="left:812px;top:559px;width:273px;height:128px;background:linear-gradient(180deg,#d19a5a,#9a5c34 60%,#3a2a20)" role="img" aria-label="Family silhouettes holding hands up at sunset"></div>
  <div class="photo" style="left:812px;top:703px;width:273px;height:127px;background:linear-gradient(135deg,#d8c3a0,#b09a78 50%,#4f88a0)" role="img" aria-label="Parents playing with their baby on a sunny beach"></div>
</section>

<!-- tagline -->
<h2 class="abs serif tagline">Tailored escapes into the world’s most vibrant cities — where culture, style, and sophistication meet</h2>

<!-- categories -->
<section class="categories">
  <div class="abs card" style="left:116px;background:linear-gradient(180deg,#8fb3c2,#8a7a62 45%,#40413a)" role="img" aria-label="Sandcastle shaped like a fairytale castle on the beach">
    <div class="card-shade"></div><div class="card-title">Brambleton Vacations<br>– Land &amp; Sea</div><div class="card-sub">Magical Getaways for all ages</div><div class="card-plus">+</div>
  </div>
  <div class="abs card" style="left:362px;background:linear-gradient(180deg,#8ab4d0,#5f8a7a 40%,#4a5d3e)" role="img" aria-label="Family walking along a coastal trail">
    <div class="card-shade"></div><div class="card-title">Family Trips</div><div class="card-sub">Memories Made Together</div><div class="card-plus">+</div>
  </div>
  <div class="abs card" style="left:608px;background:linear-gradient(180deg,#9eb6c4,#6b7558 40%,#5d6b3c)" role="img" aria-label="Couple standing by a vintage truck in open countryside">
    <div class="card-shade"></div><div class="card-title">Texas Road Trips</div><div class="card-sub">Explore Texas with Ease</div><div class="card-plus">+</div>
  </div>
  <div class="abs card" style="left:852px;background:linear-gradient(180deg,#c8d4c8,#8a9a86 40%,#56655a)" role="img" aria-label="Traveler in a sun hat holding up a map">
    <div class="card-shade"></div><div class="card-title">Other<br>Destinations</div><div class="card-sub">Beyond the Ordinary</div><div class="card-plus">+</div>
  </div>
</section>

<!-- why choose us -->
<section>
  <div class="abs why"></div>
  <div class="abs eyebrow" style="left:117px;top:1433px">WHY CHOOSE US</div>
  <h2 class="abs serif why-title">Crafting journeys as unique as you—seamless, personal, unforgettable.</h2>

  <div class="abs feature" style="left:114px">
    <svg width="62" height="64" viewBox="0 0 62 64" fill="none" stroke="#c0923f" stroke-width="2"><circle cx="31" cy="22" r="12"/><circle cx="31" cy="22" r="4"/><path d="M31 34v10M6 46l12-6 13 6 13-6 12 6-4 14H10z"/></svg>
    <div class="feature-title">LOCAL &amp;<br>PERSONAL</div>
    <div class="feature-text">We’re your neighbors, not a call center</div>
    <div class="feature-num serif">1</div>
  </div>
  <div class="abs feature" style="left:440px">
    <svg width="62" height="64" viewBox="0 0 62 64" fill="none" stroke="#c0923f" stroke-width="2"><path d="M18 60V46c-6-4-9-10-9-17 0-12 10-21 22-21s22 9 22 21c0 5-2 8-4 10l4 8h-6v8H34v5"/><path d="M31 40l-8-8a5 5 0 0 1 8-6 5 5 0 0 1 8 6z"/></svg>
    <div class="feature-title">STRESS-FREE<br>PLANNING</div>
    <div class="feature-text">We’re your neighbors, not a call center</div>
    <div class="feature-num serif">2</div>
  </div>
  <div class="abs feature" style="left:767px">
    <svg width="62" height="64" viewBox="0 0 62 64" fill="none" stroke="#c0923f" stroke-width="2"><path d="M31 4l14 6v10c0 9-6 15-14 19-8-4-14-10-14-19V10z"/><path d="M24 20l5 5 9-9"/><path d="M4 40l12-4 10 6h10l6 4-6 4H24l14 2 16-8 4 4-20 12H16l-12-6"/></svg>
    <div class="feature-title">TRUSTED TRAVEL<br>EXPERTISE</div>
    <div class="feature-text">Curated trips tailored just for you</div>
    <div class="feature-num serif">3</div>
  </div>
</section>

<!-- community -->
<section>
  <div class="abs community" role="img" aria-label="Mother embracing her smiling son by a sunlit lake"></div>
  <svg class="abs" style="left:550px;top:1866px" width="160" height="140" viewBox="0 0 160 140" fill="none" stroke="#fff" stroke-width="2.5"><path d="M12 132C0 90 30 30 80 18s60-10 66-4" stroke-dasharray="7 6"/><circle cx="12" cy="132" r="6" fill="none"/><circle cx="150" cy="18" r="6" fill="none"/></svg>
  <h2 class="abs serif community-title">Proudly Serving Our<br>Local Community</h2>
  <p class="abs community-text">Based in Texas, we specialize in creating unforgettable journeys for families and travelers just like you.</p>
  <a class="abs btn-light" href="#" style="left:613px;top:2106px;width:205px;height:33px">LEARN MORE ABOUT US</a>
</section>

<!-- blogs -->
<section>
  <h2 class="abs eyebrow blogs-head">LATEST BLOGS</h2>
  <div class="abs view-all">VIEW ALL
    <svg width="24" height="14" viewBox="0 0 24 14" fill="none" stroke="#1d5566" stroke-width="1.5"><path d="M7 1L1 7l6 6M17 1l6 6-6 6"/></svg>
  </div>
  <article class="abs blog" style="left:118px">
    <div class="photo" style="background:linear-gradient(135deg,#d8d4c6,#b9c2b6 50%,#8aa3b0)" role="img" aria-label="Model airplane and compass on a world map"></div>
    <h3 class="blog-title">Top 10 Must-Visit<br>Destinations for 2026</h3>
    <div class="blog-more">LEARN MORE</div>
  </article>
  <article class="abs blog" style="left:445px">
    <div class="photo" style="background:linear-gradient(135deg,#2a3036,#6f5a36 50%,#c9a660)" role="img" aria-label="Scratch-off world map with a toy airplane"></div>
    <h3 class="blog-title">The Ultimate Travel Planning<br>Guide: From Dream to Departure</h3>
    <div class="blog-more">LEARN MORE</div>
  </article>
  <article class="abs blog" style="left:773px">
    <div class="photo" style="background:linear-gradient(180deg,#3d5470,#6a7590 45%,#2b3140)" role="img" aria-label="Seaside promenade with yachts at dusk"></div>
    <h3 class="blog-title">Luxury vs Budget Travel: How to<br>Choose the Perfect Experience</h3>
    <div class="blog-more">LEARN MORE</div>
  </article>
</section>

<!-- call to action -->
<section>
  <div class="abs cta-photo" role="img" aria-label="Traveling couple with luggage outside an airport terminal"></div>
  <div class="abs cta-box"></div>
  <div class="abs cta-badge"><span class="brand-dot"></span>Meander &amp; Maple</div>
  <h2 class="abs serif cta-title">Your next journey starts with a conversation—get in touch today.</h2>
  <p class="abs cta-text">Questions, plans, or bookings—we’re here<br>to make travel easy.</p>
  <a class="abs btn-teal" href="#">CONTACT US NOW</a>
</section>

<!-- footer -->
<footer>
  <div class="abs footer"></div>
  <div class="abs footer-brand"><span class="brand-dot"></span>Meander &amp; Maple</div>
  <span class="abs social" style="left:221px" aria-label="Social profile"></span>
  <span class="abs social" style="left:255px" aria-label="Social profile"></span>

  <div class="abs foot-col" style="left:484px">
    <h4>NAVIGATION</h4>
    <ul><li>Brambleton Vacations</li><li>Family Trips</li><li>Texas Road Trips</li><li>Other Destinations</li><li>About Us</li><li>Contact Us</li></ul>
  </div>
  <div class="abs foot-col" style="left:657px">
    <h4>QUICK LINKS</h4>
    <ul><li>Brambleton Vacations</li><li>Family Trips</li><li>Texas Road Trips</li><li>Other Destinations</li><li>About Us</li><li>Contact Us</li></ul>
  </div>
  <div class="abs foot-col" style="left:855px">
    <h4 style="margin-bottom:20px">CONTACT US</h4>
    <div class="contact-line">
      <span class="contact-icon"><svg width="12" height="12" viewBox="0 0 24 24"><path d="M6 2l4 5-2 3c1 3 4 6 7 7l3-2 5 4-3 4C11 22 2 13 2 5z" fill="#fff"/></svg></span>
      <span class="phone">555.010.2024</span>
    </div>
    <div class="contact-line">
      <span class="contact-icon"><svg width="12" height="10" viewBox="0 0 24 18" fill="none" stroke="#fff" stroke-width="2.5"><rect x="1" y="1" width="22" height="16"/><path d="M1 1l11 9 11-9"/></svg></span>
      <span class="email">hello@meanderandmaple.com</span>
    </div>
  </div>
  <p class="abs copyright">© 2026 Meander &amp; Maple Travel Co. All Rights Reserved.</p>
</footer>

</body>
</html>
```